Front cover of trifold brochure

This is for my real estate company. I need a design for the front page of the tri fold brochure. The interior of the brochure will constantly change, however I wanted to update the front cover to something more modern. I sell high end vacation homes on a Grand Lake, located in Northeast Oklahoma. So something that would appeal to vacation/second lake home buyers would be great. My logo colors are orange and burgundy, if we could incorporate those colors that would be great. I have attached a zip drive with all of the versions of my logo. I want to have a logo on there, as well as my phone number and my website. My website is www.tresslowandco.com, and my office number is 555-310-4826.

```html
<!DOCTYPE html>
<html lang="en">
<head>
<meta charset="utf-8">
<title>Grand Lake Waterfront Property – Trifold Cover</title>
<link href="https://fonts.googleapis.com/css2?family=Open+Sans:wght@400;600;700&display=swap" rel="stylesheet">
<style>
  :root{
    --burgundy:#7d1142;
    --orange:#e07a12;
    --yellow:#e8c21a;
    --paper:#ffffff;
    --backdrop:#a9a9a9;
    --ink:#2b2b2b;
  }
  html,body{margin:0;padding:0;width:900px;height:1200px;overflow:hidden;background:var(--backdrop);}
  body{font-family:"Open Sans",sans-serif;color:var(--ink);}
  .spread{position:absolute;left:30px;top:276px;width:840px;height:648px;background:var(--paper);box-shadow:0 10px 30px rgba(0,0,0,.25);}
  .spread-art{position:absolute;inset:0;}
  .fold{position:absolute;top:0;bottom:0;width:1px;background:rgba(0,0,0,.08);}
  .about{position:absolute;left:28px;top:462px;width:226px;}
  .about h2{margin:0 0 6px;font-size:13px;font-weight:700;color:var(--burgundy);}
  .about h2::after{content:"";display:block;width:24px;height:2px;background:var(--orange);margin-top:3px;}
  .about p{margin:0;font-size:9.5px;line-height:1.55;text-align:justify;}
  .contact{position:absolute;left:280px;top:462px;width:280px;text-align:center;}
  .contact .company{margin:0 0 12px;font-size:13px;font-weight:700;color:var(--burgundy);}
  .contact-item{margin:0 0 8px;font-size:11px;}
  .contact-item svg{display:block;margin:0 auto 2px;}
  .brand{position:absolute;left:620px;top:42px;display:flex;align-items:center;gap:8px;}
  .brand-mark{width:26px;height:26px;background:var(--orange);}
  .brand-name{font-size:15px;font-weight:600;color:var(--burgundy);line-height:1.1;}
  .title{position:absolute;left:592px;top:474px;width:230px;}
  .title-line{display:block;font-weight:700;line-height:1;}
  .title-lake{font-size:30px;color:var(--orange);}
  .title-waterfront{font-size:30px;color:var(--burgundy);}
  .title-property{font-size:17px;font-weight:400;letter-spacing:11px;color:var(--burgundy);margin-top:4px;}
</style>
</head>
<body>
<div class="spread">
  <svg class="spread-art" width="840" height="648" viewBox="0 0 840 648">
    <defs>
      <linearGradient id="photoTones" x1="0" y1="0" x2="0" y2="1">
        <stop offset="0" stop-color="#cfe0ea"/>
        <stop offset="0.3" stop-color="#6f8f6a"/>
        <stop offset="0.55" stop-color="#5aaed8"/>
        <stop offset="1" stop-color="#c9ccca"/>
      </linearGradient>
      <linearGradient id="edgeTone" x1="0" y1="0" x2="1" y2="0">
        <stop offset="0" stop-color="var(--yellow)"/>
        <stop offset="1" stop-color="var(--orange)"/>
      </linearGradient>
    </defs>
    <path d="M0,162 C150,128 250,138 420,172 S700,128 840,108" fill="none" stroke="var(--orange)" stroke-width="4"/>
    <g role="img" aria-label="Photo of a lakeside resort pool with sun shades, lounge chairs and Grand Lake beyond">
      <path d="M0,175 C150,140 250,150 420,185 S700,140 840,120 L840,430 C700,455 560,440 420,420 S140,400 0,395 Z" fill="url(#photoTones)"/>
    </g>
    <path d="M0,395 C140,400 280,400 420,420 S700,455 840,430 L840,466 C700,490 560,476 420,456 S140,432 0,430 Z" fill="var(--burgundy)"/>
    <rect x="0" y="642" width="840" height="6" fill="url(#edgeTone)"/>
  </svg>
  <div class="fold" style="left:280px"></div>
  <div class="fold" style="left:560px"></div>

  <section class="about">
    <h2>About</h2>
    <p>Tresslow &amp; Co. Realty welcomes you to Grand Lake – a destination of great natural beauty and family fun. We look forward to being your resource for buying and selling real estate in this gorgeous Northeast region of Oklahoma. Our unrivaled expertise in Grand Lake waterfront property makes us one of the most popular realtor teams around.</p>
  </section>

  <section class="contact">
    <p class="company">Tresslow &amp; Company Realty</p>
    <p class="contact-item">
      <svg width="12" height="12" viewBox="0 0 12 12"><path d="M6 11 C3 7 2.5 5.5 2.5 4.5 A3.5 3.5 0 0 1 9.5 4.5 C9.5 5.5 9 7 6 11Z" fill="none" stroke="var(--orange)" stroke-width="1.2"/><circle cx="6" cy="4.5" r="1.2" fill="var(--orange)"/></svg>
      Northeast Oklahoma</p>
    <p class="contact-item">
      <svg width="12" height="12" viewBox="0 0 12 12"><circle cx="6" cy="6" r="5.2" fill="none" stroke="var(--orange)" stroke-width="1"/><path d="M4 3.5 L5 3.3 L5.6 5 L5 5.5 C5.4 6.4 5.9 6.9 6.7 7.2 L7.2 6.6 L8.7 7.3 L8.5 8.3 C6 8.5 3.8 6.2 4 3.5Z" fill="var(--orange)"/></svg>
      555-310-4826</p>
    <p class="contact-item">
      <svg width="12" height="12" viewBox="0 0 12 12"><rect x="1.5" y="3" width="9" height="6.5" fill="none" stroke="var(--orange)" stroke-width="1.1"/><path d="M1.5 3 L6 7 L10.5 3" fill="none" stroke="var(--orange)" stroke-width="1.1"/></svg>
      hello@tresslow.net</p>
    <p class="contact-item">
      <svg width="12" height="12" viewBox="0 0 12 12"><circle cx="6" cy="6" r="5" fill="none" stroke="var(--orange)" stroke-width="1.1"/><ellipse cx="6" cy="6" rx="2.2" ry="5" fill="none" stroke="var(--orange)" stroke-width="1"/><path d="M1 6 H11" stroke="var(--orange)" stroke-width="1"/></svg>
      www.tresslowandco.com</p>
  </section>

  <div class="brand">
    <span class="brand-mark"></span>
    <span class="brand-name">Tresslow<br>&amp; Company Realty</span>
  </div>

  <h1 class="title">
    <span class="title-line title-lake">GRAND LAKE</span>
    <span class="title-line title-waterfront">WATERFRONT</span>
    <span class="title-line title-property">PROPERTY</span>
  </h1>
</div>
</body>
</html>
```